"Velvet Crest" sexual performance enhancement pill bottle label needed.

This should be interesting...

I am starting a line of sexual performance enhancement products. This will be the first of several products basically. Keep in mind, I am the type of business person to stay with one company for years if they provide me with quality work.

This particular product is a male sexual performance pill. The name of the product is "Velvet Crest." The packaging of the pills are a black bottle with a white top. Label on the product example would be perfect but at a minimum I have attached a "template" for your guidance.

Some of the technical aspects of this are as follows:

-File Format: Illustrator CS6 is preferred. (Winner must provide artwork in layer and can not flatten artwork.)
-Resolution: 300 dpi minimum
-Bleed: 1/16th (0.0625") inch from edge of label
-Color Mode: CMYK only or must be converted to CMYK for final production

Lastly, this is your project as a designer, artist, creator, this is essentially a piece of you that will be sold and known by thousands of people. I have no color scheme that I prefer, just use the template and follow the layout. If you have any further questions, please feel free to contact me at any time.
Updates

Quick note on the product and what it does: -Powerful, long lasting, harder erections -Works in a minutes and last for hours -Enhances sexual desire and drive Thank you for your ideas...

Project Deadline Extended
Reason: We decided to extent the project for a few more days to let the last few concepts come in. So far things are looking really good and we definitely have seen some amazing designs. Thank you for your hard work and amazing creativity. Looking forward to seeing what we have come in the next couple of day. Very respectfully, Brock

ONLY THREE DAYS LEFT!!!! Please submit your ideas as soon as possible. And as always, thank you for your help!!! V/r, Brock

Industry/Entity Type

Graphic Design

```html
<!DOCTYPE html>
<html lang="en">
<head>
<meta charset="utf-8">
<title>Velvet Crest – Bottle Label</title>
<link href="https://fonts.googleapis.com/css2?family=Bebas+Neue&family=Arimo:wght@400;700&family=Open+Sans:wght@300;400;600;700&display=swap" rel="stylesheet">
<style>
  :root {
    --label-black: #000000;
    --ink-white: #ffffff;
    --accent-red: #e8141b;
    --accent-red-dark: #9c0d11;
    --page: #ffffff;
  }
  * { box-sizing: border-box; margin: 0; padding: 0; }
  html, body { width: 1200px; height: 848px; overflow: hidden; background: var(--page); }
  .canvas { position: relative; width: 1200px; height: 848px; background: var(--page); }
  .label {
    position: absolute; left: 0; top: 0; width: 1200px; height: 470px;
    background: var(--label-black); color: var(--ink-white);
    font-family: "Open Sans", sans-serif;
  }
  .abs { position: absolute; }

  .brand-name {
    font-family: "Bebas Neue", sans-serif; font-weight: 400;
    font-size: 72px; line-height: 1; letter-spacing: 0.5px; text-align: center;
    width: 440px; white-space: nowrap;
  }
  .brand-tag {
    font-family: "Arimo", sans-serif; font-weight: 700;
    color: var(--accent-red); font-size: 22px; line-height: 1; text-align: right;
    white-space: nowrap;
  }
  .front .brand-name { left: 77px; top: 30px; }
  .front .brand-tag { left: 220px; width: 203px; top: 97px; }
  .emblem-area {
    left: 175px; top: 145px; width: 255px; height: 212px;
    background: radial-gradient(circle at 60% 45%, var(--accent-red), var(--accent-red-dark));
    border-radius: 50% 50% 6px 6px / 60% 60% 6px 6px;
  }
  .front-claim {
    left: 60px; top: 382px; width: 480px; text-align: center; white-space: nowrap;
    font-family: "Bebas Neue", sans-serif; font-weight: 400; font-size: 64px; line-height: 1;
  }
  .side-text {
    font-family: "Bebas Neue", sans-serif; font-weight: 400; font-size: 22px;
    writing-mode: vertical-rl; white-space: nowrap; line-height: 1;
  }
  .count-side { left: 26px; top: 186px; }
  .food-side { left: 589px; top: 180px; }

  .back .brand-name { left: 679px; top: 28px; }
  .back .brand-tag { left: 822px; width: 203px; top: 95px; }

  .directions {
    left: 648px; top: 170px; width: 138px;
    font-size: 4.6px; line-height: 1.3; text-align: justify;
  }
  .directions p { margin-bottom: 2px; }
  .directions strong { font-weight: 700; }
  .fda-note {
    margin: 3px 0 8px; background: var(--ink-white); color: var(--label-black);
    padding: 2px 3px; font-size: 4.4px;
  }
  .maker { font-size: 5.6px; font-weight: 700; line-height: 1.35; }

  .product-title {
    left: 790px; top: 156px; width: 225px; text-align: center;
    font-family: "Open Sans", sans-serif; font-weight: 300; font-size: 35px; line-height: 40px;
  }
  .product-claims {
    left: 790px; top: 292px; width: 225px; text-align: center;
    font-size: 8.5px; line-height: 20px;
  }
  .product-count {
    left: 790px; top: 341px; width: 225px; text-align: center;
    font-size: 9px; font-weight: 700;
  }

  .facts {
    left: 1030px; top: 168px; width: 121px; border: 1.5px solid var(--ink-white);
    padding: 2px 3px; font-size: 5px; line-height: 1.3;
  }
  .facts-title { font-size: 12px; line-height: 1.1; border-bottom: 2px solid var(--ink-white); padding-bottom: 2px; }
  .facts-row { display: flex; justify-content: space-between; }
  .facts-sep { border-top: 1px solid var(--ink-white); margin: 2px 0; }
  .facts-blend { text-align: justify; }
  .other-ingredients { left: 1030px; top: 290px; width: 124px; font-size: 4.8px; line-height: 1.3; }

  .site-url {
    left: 760px; top: 420px; width: 280px; text-align: center; white-space: nowrap;
    font-family: "Bebas Neue", sans-serif; font-weight: 400; font-size: 22px; line-height: 1;
  }
</style>
</head>
<body>
<div class="canvas">
  <section class="label">
    <div class="front">
      <h1 class="abs brand-name">VELVET CREST</h1>
      <div class="abs brand-tag">POWERFUL</div>
      <div class="abs emblem-area" role="img" aria-label="Red brand emblem area"></div>
      <div class="abs front-claim">MAXIMUM POTENCY</div>
      <div class="abs side-text count-side">60 CAPSULES</div>
    </div>

    <div class="abs side-text food-side">FOOD SUPPLEMENT</div>

    <div class="back">
      <h2 class="abs brand-name">VELVET CREST</h2>
      <div class="abs brand-tag">POWERFUL</div>

      <div class="abs directions">
        <p><strong>SUGGESTED USE:</strong> As a dietary supplement, take two (2) capsules 1 hour before physical activity, or as directed by your health care professional. Do not exceed two (2) capsules daily.</p>
        <p><strong>CAUTION:</strong> Do not exceed recommended dose. This product is not intended for pregnant or nursing mothers, children under the age of 18, or individuals taking prescription drugs. Discontinue use immediately if nausea, sleeplessness, or nervousness occur. Do not take this product if you have a known medical condition including high blood pressure, diabetes, any cardiovascular disorder, heart disease, hyperthyroidism, or are taking anti-depressant medications. If you have questions about the advisability of taking this product, consult your physician prior to use.</p>
        <p><strong>KEEP OUT OF THE REACH OF CHILDREN. DO NOT USE IF SAFETY SEAL IS DAMAGED OR MISSING. STORE AT ROOM TEMPERATURE.</strong></p>
        <div class="fda-note">* These statements have not been evaluated by the Food and Drug Administration. This product is not intended to diagnose, treat, cure or prevent any disease.</div>
        <div class="maker">Manufactured Exclusively For:<br>COMPANY INFO</div>
      </div>

      <div class="abs product-title">Horny<br>Goat Weed<br>1600</div>
      <div class="abs product-claims">Max Strength!<br>Pure and Potent*</div>
      <div class="abs product-count">Dietary Supplement · 60 Capsules</div>

      <div class="abs facts">
        <div class="facts-title">Supplement Facts</div>
        <div><strong>Serving Size: 2 Capsules</strong></div>
        <div><strong>Servings Per Container: 30</strong></div>
        <div class="facts-sep"></div>
        <div class="facts-row"><span>Amount Per Serving</span><span>% Daily Value</span></div>
        <div class="facts-sep"></div>
        <div class="facts-row"><strong>VCX-Rx™ Proprietary Formula</strong><strong>1,360 mg †</strong></div>
        <div class="facts-blend">Horny Goat Weed (herb powder), Maca (herb powder), Mucuna Pruriens (L-Dopa), Polypodium Vulgare (herb powder), Yohimbe Bark (herb powder), Saw Palmetto (herb powder), Muira Puama (herb powder), Arginine (L-Arginine hydrochloride), Panax Ginseng (herb powder)</div>
        <div class="facts-sep"></div>
        <div>† % Daily Value not established</div>
      </div>
      <div class="abs other-ingredients"><strong>Other Ingredients:</strong> Gelatin, Magnesium Stearate, and Calcium Carbonate.</div>

      <div class="abs site-url">WWW.VELVETCRESTPILL.COM</div>
    </div>
  </section>
</div>
</body>
</html>
```